Website Design For Ecommerce Brand That Sells Personalized Wall Decor

We need a new website for our company Copper Lantern. Our current site is functioning through wordpress/woocomerce but we are not happy with the appearance. Our products really wow people when they receive them and we need your help making our website do the same!

Number of Pages Required

4 page

```html
<!DOCTYPE html>
<html lang="en">
<head>
<meta charset="utf-8">
<title>Copper Lantern — Personalized Wall Decor</title>
<link href="https://fonts.googleapis.com/css2?family=Dancing+Script:wght@700&family=Roboto+Condensed:ital,wght@0,400;0,700;1,400&display=swap" rel="stylesheet">
<style>
:root{
  --ink:#1e1409;
  --card:#1a1107;
  --gold:#e6c25a;
  --gold-soft:#f0d27a;
  --amber:#c99320;
  --panel:#5e3e06;
  --frame:#8a5a0f;
  --paper:#ffffff;
  --text:#1d1d1d;
  --muted:#777;
}
*{box-sizing:border-box;margin:0;padding:0}
html,body{width:1200px;height:3438px;overflow:hidden}
body{position:relative;background:var(--paper);font-family:"Roboto Condensed",sans-serif;color:var(--text)}
.script{font-family:"Dancing Script",cursive;font-weight:700;color:var(--amber)}
.section-title{position:absolute;left:0;width:1200px;text-align:center;font-size:44px}

.site-header{position:absolute;left:0;top:0;width:1200px;height:64px;background:var(--ink)}
.main-nav{position:absolute;left:88px;top:22px;display:flex;gap:28px;color:#fff;font-weight:700;font-size:15px}
.header-icons{position:absolute;right:88px;top:20px;display:flex;gap:16px}
.brand-badge{position:absolute;left:50%;transform:translateX(-50%);width:160px;height:160px;border-radius:50%;background:var(--paper);border:10px solid #5a4426;box-shadow:0 0 0 4px var(--paper);display:flex;align-items:center;justify-content:center;text-align:center}
.brand-badge span{font-size:22px;font-weight:700;color:var(--ink);line-height:1.05}

.hero{position:absolute;left:0;top:64px;width:1200px;height:496px;background:#3a2814}
.hero-left{position:absolute;left:0;top:0;width:770px;height:496px;background:linear-gradient(180deg,#b9c3cc 0%,#d8cfbf 55%,#7a5634 62%,#5a3b20 100%)}
.hero-right{position:absolute;left:778px;top:0;width:422px;height:496px;background:linear-gradient(135deg,#5b3620,#3a2414 60%,#4e2e19)}
.hero-box{position:absolute;left:320px;top:160px;width:560px;height:246px;background:rgba(35,24,8,.88);text-align:center}
.hero-box h1{font-family:"Dancing Script",cursive;font-size:50px;color:var(--gold);line-height:1.05;margin-top:30px;font-weight:700}
.btn-outline{display:inline-block;margin-top:22px;padding:8px 42px;border:1.5px solid var(--gold);border-radius:22px;color:var(--gold);font-size:16px;letter-spacing:1px}
.hero-dots{position:absolute;left:570px;top:468px;display:flex;gap:12px;align-items:center}
.hero-dots i{width:7px;height:7px;border-radius:50%;background:#222}
.hero-dots i.on{width:14px;height:14px;border:2px solid var(--gold);background:#a87d26}

.cat{position:absolute;top:709px;width:144px;text-align:center}
.cat .thumb{width:144px;height:135px}
.cat h3{font-size:14px;font-weight:400;margin-top:12px;color:#222}
.cat small{font-size:12px;font-style:italic;color:var(--muted)}
.arrow{position:absolute;width:46px;height:46px;border-radius:50%;display:flex;align-items:center;justify-content:center}
.arrow.dark{background:var(--ink);box-shadow:0 0 0 6px #f3e7c2}
.arrow.gold{background:var(--gold);box-shadow:0 0 0 6px #f5ecd0}
.arrow.ring{background:#3b2a12;box-shadow:0 0 0 4px #5b4524}

.best-selling{position:absolute;left:0;top:965px;width:1200px;height:662px;background:radial-gradient(ellipse at 50% 40%,#3b2a16,#1f150a 75%)}
.product{position:absolute;width:292px;height:353px;background:var(--card);text-align:center;color:#fff}
.product .photo{width:200px;height:200px;border-radius:50%;margin:32px auto 0;border:1.5px solid var(--amber);outline:6px solid var(--card)}
.product p{font-size:15px;line-height:21px;margin:20px 22px 0}
.product b{display:block;color:var(--gold);font-size:18px;margin-top:14px}
.btn-gold{position:absolute;left:537px;width:126px;height:37px;border-radius:20px;background:var(--gold);color:var(--ink);font-weight:700;font-size:13px;display:flex;align-items:center;justify-content:center;gap:10px}

.feature-photo{position:absolute;left:0;top:2289px;width:663px;height:436px;background:linear-gradient(90deg,#c9d2dc 0%,#9b7a4a 22%,#3d2a1c 40%,#3a281b 75%,#8d6a3a 100%)}
.feature-frame{position:absolute;left:628px;top:2348px;width:484px;height:332px;border:3px solid var(--frame)}
.feature-panel{position:absolute;left:626px;top:2365px;width:470px;height:300px;background:var(--panel);text-align:center;color:#fff}
.feature-panel h2{font-family:"Dancing Script",cursive;font-size:40px;line-height:44px;color:var(--gold-soft);margin-top:52px}
.feature-panel p{font-size:14px;line-height:25px;margin-top:8px}

.touch-copy{position:absolute;left:200px;top:2862px;width:800px;text-align:center;font-size:13.5px;line-height:23px;color:#222}

.site-footer{position:absolute;left:0;top:3105px;width:1200px;height:295px;background:var(--ink)}
.footer-nav{position:absolute;left:0;top:145px;width:1200px;display:flex;justify-content:center;gap:25px;font-size:14px;color:#eee}
.footer-nav .current{color:var(--gold);border-bottom:1px solid var(--gold)}
.contact-item{position:absolute;top:195px;display:flex;align-items:center;gap:14px;color:var(--gold);font-size:16px;line-height:20px;text-decoration:underline}
.to-top{position:absolute;left:1113px;top:3242px;width:56px;height:56px;border-radius:50%;background:var(--gold);display:flex;align-items:center;justify-content:center}
.legal-bar{position:absolute;left:0;top:3400px;width:1200px;height:38px;background:var(--gold);display:flex;align-items:center;justify-content:space-between;padding:0 88px;font-size:14px;color:var(--ink)}
.pay-list{display:flex;gap:16px;font-weight:700}
</style>
</head>
<body>

<header class="site-header">
  <nav class="main-nav"><span>Products ▾</span><span>FAQ</span><span>Contact Us</span></nav>
  <div class="header-icons">
    <svg width="22" height="22" viewBox="0 0 22 22" fill="none" stroke="#e6c25a" stroke-width="2"><circle cx="9" cy="9" r="7"/><path d="M14 14l6 6"/></svg>
    <svg width="22" height="22" viewBox="0 0 24 22" fill="none" stroke="#e6c25a" stroke-width="2"><path d="M12 20S2 13 2 7a5 5 0 0 1 10-1 5 5 0 0 1 10 1c0 6-10 13-10 13z"/></svg>
    <svg width="20" height="22" viewBox="0 0 20 22" fill="none" stroke="#e6c25a" stroke-width="2"><circle cx="10" cy="7" r="5"/><path d="M2 21c0-5 4-8 8-8s8 3 8 8"/></svg>
    <svg width="26" height="24" viewBox="0 0 26 24" fill="none" stroke="#e6c25a" stroke-width="2"><path d="M1 2h4l3 14h14l3-10H7"/><circle cx="10" cy="21" r="2"/><circle cx="20" cy="21" r="2"/></svg>
  </div>
</header>

<section class="hero">
  <div class="hero-left" role="img" aria-label="Layered wooden family tree sign with names on a shelf"></div>
  <div class="hero-right" role="img" aria-label="Personalized wooden dinosaur ornaments with names on dark wood"></div>
  <div class="hero-box">
    <h1>Welcome To<br>Copper Lantern!</h1>
    <span class="btn-outline">Shop Now</span>
  </div>
  <div class="hero-dots"><i></i><i></i><i class="on"></i></div>
</section>
<div class="brand-badge" style="top:8px"><span>COPPER<br>LANTERN</span></div>

<h2 class="section-title script" style="top:628px">Browse by Category</h2>
<div class="arrow dark" style="left:54px;top:757px"><svg width="12" height="14" viewBox="0 0 12 14"><path d="M9 1L3 7l6 6" stroke="#e6c25a" stroke-width="2.5" fill="none"/></svg></div>
<div class="cat" style="left:176px"><div class="thumb" role="img" aria-label="Framed family tree sign" style="background:linear-gradient(135deg,#4a3524,#8a6d50)"></div><h3>New Arrivals</h3><small>32 Items</small></div>
<div class="cat" style="left:352px"><div class="thumb" role="img" aria-label="Personalized grandkids wooden sign" style="background:linear-gradient(135deg,#7a4a34,#e2cdb4)"></div><h3>Personalized Gifts</h3><small>32 Items</small></div>
<div class="cat" style="left:528px"><div class="thumb" role="img" aria-label="Wooden name ornament" style="background:linear-gradient(135deg,#4a2f1c,#8a5d3a)"></div><h3>Home Decor</h3><small>32 Items</small></div>
<div class="cat" style="left:704px"><div class="thumb" role="img" aria-label="White wooden gnome decoration" style="background:linear-gradient(90deg,#3a2414,#e8e4dc 50%,#3a2414)"></div><h3>Gnome</h3><small>32 Items</small></div>
<div class="cat" style="left:880px"><div class="thumb" role="img" aria-label="Wooden heart name cutouts" style="background:linear-gradient(135deg,#f2ece2,#c9a273)"></div><h3>Craft Supplies</h3><small>32 Items</small></div>
<div class="arrow gold" style="left:1100px;top:757px"><svg width="12" height="14" viewBox="0 0 12 14"><path d="M3 1l6 6-6 6" stroke="#1e1409" stroke-width="2.5" fill="none"/></svg></div>

<section class="best-selling" aria-label="Best Selling"></section>
<h2 class="section-title script" style="top:1033px;color:var(--gold)">Best Selling</h2>
<div class="arrow ring" style="left:49px;top:1269px"><svg width="12" height="14" viewBox="0 0 12 14"><path d="M9 1L3 7l6 6" stroke="#e6c25a" stroke-width="2.5" fill="none"/></svg></div>
<article class="product" style="left:137px;top:1116px"><div class="photo" role="img" aria-label="Pet memorial plaque" style="background:radial-gradient(#f1e6d4,#b6a38a)"></div><p>In Memory of Lost Pet Plaque, Custom Memorial Sign Gift for...</p><b>$20.00 – $25.00</b></article>
<article class="product" style="left:454px;top:1116px"><div class="photo" role="img" aria-label="Halloween wooden lamp" style="background:radial-gradient(#e9a24a,#1d2330 70%)"></div><p>Halloween Wooden Lamp, Jack O Lantern, Laser Cut Lamp, Halloween...</p><b>$20.00 – $25.00</b></article>
<article class="product" style="left:770px;top:1116px"><div class="photo" role="img" aria-label="Pink pet memorial ornament" style="background:radial-gradient(#e4a9a0,#8b4a3c)"></div><p>12 Inch Square Framed Personalized Family Tree Wall Decor...</p><b>$16.00</b></article>
<div class="arrow ring" style="left:1097px;top:1269px"><svg width="12" height="14" viewBox="0 0 12 14"><path d="M3 1l6 6-6 6" stroke="#e6c25a" stroke-width="2.5" fill="none"/></svg></div>
<div class="btn-gold" style="top:1510px">View More <svg width="12" height="12" viewBox="0 0 12 12"><circle cx="6" cy="6" r="6" fill="#1e1409"/><path d="M3 6h5M6 3.5L8.5 6 6 8.5" stroke="#e6c25a" stroke-width="1.5" fill="none"/></svg></div>

<h2 class="section-title script" style="top:1694px">Top Rated</h2>
<div class="arrow gold" style="left:49px;top:1930px;background:#fff;box-shadow:0 0 0 6px #f5ecd0"><svg width="12" height="14" viewBox="0 0 12 14"><path d="M9 1L3 7l6 6" stroke="#1e1409" stroke-width="2.5" fill="none"/></svg></div>
<article class="product" style="left:137px;top:1777px"><div class="photo" role="img" aria-label="Pet memorial plaque" style="background:radial-gradient(#f1e6d4,#b6a38a)"></div><p>In Memory of Lost Pet Plaque, Custom Memorial Sign Gift for...</p><b>$20.00 – $25.00</b></article>
<article class="product" style="left:454px;top:1777px"><div class="photo" role="img" aria-label="Halloween wooden lamp" style="background:radial-gradient(#e9a24a,#1d2330 70%)"></div><p>Halloween Wooden Lamp, Jack O Lantern, Laser Cut Lamp, Halloween...</p><b>$20.00 – $25.00</b></article>
<article class="product" style="left:770px;top:1777px"><div class="photo" role="img" aria-label="Pink pet memorial ornament" style="background:radial-gradient(#e4a9a0,#8b4a3c)"></div><p>12 Inch Square Framed Personalized Family Tree Wall Decor...</p><b>$16.00</b></article>
<div class="arrow gold" style="left:1097px;top:1930px"><svg width="12" height="14" viewBox="0 0 12 14"><path d="M3 1l6 6-6 6" stroke="#1e1409" stroke-width="2.5" fill="none"/></svg></div>
<div class="btn-gold" style="top:2171px">View More <svg width="12" height="12" viewBox="0 0 12 12"><circle cx="6" cy="6" r="6" fill="#1e1409"/><path d="M3 6h5M6 3.5L8.5 6 6 8.5" stroke="#e6c25a" stroke-width="1.5" fill="none"/></svg></div>

<div class="feature-photo" role="img" aria-label="Framed wooden family tree sign with names beside greenery"></div>
<div class="feature-frame"></div>
<div class="feature-panel">
  <h2>Personalize the<br>Family Tree</h2>
  <p>See the preview before purchasing<br>(beta version still has bugs)</p>
  <div class="btn-gold" style="left:172px;top:206px">Shop Now <svg width="12" height="12" viewBox="0 0 12 12"><circle cx="6" cy="6" r="6" fill="#1e1409"/><path d="M3 6h5M6 3.5L8.5 6 6 8.5" stroke="#e6c25a" stroke-width="1.5" fill="none"/></svg></div>
</div>

<h2 class="section-title script" style="top:2793px">Get in Touch</h2>
<p class="touch-copy">Lorem Ipsum is simply dummy text of the printing and typesetting industry. Lorem Ipsum has been the industry's standard dummy text ever since the 1500s, when an unknown printer took a galley of type and scrambled it to make a type specimen book.</p>
<div class="btn-gold" style="top:2933px;left:527px;width:136px">Enquire Now <svg width="12" height="12" viewBox="0 0 12 12"><circle cx="6" cy="6" r="6" fill="#1e1409"/><path d="M3 6h5M6 3.5L8.5 6 6 8.5" stroke="#e6c25a" stroke-width="1.5" fill="none"/></svg></div>

<footer class="site-footer">
  <nav class="footer-nav"><span class="current">Home</span><span>Home Decor</span><span>Gnome</span><span>Personalized Gifts</span><span>Craft Supplies</span><span>Pre-Cut Shapes</span><span>Unfinished Wood</span><span>Halloween</span></nav>
  <div class="contact-item" style="left:150px"><svg width="38" height="38" viewBox="0 0 38 38" fill="none" stroke="#e6c25a" stroke-width="2"><path d="M19 33s-9-10-9-17a9 9 0 0 1 18 0c0 7-9 17-9 17z"/><circle cx="19" cy="16" r="3.5"/><path d="M8 28c-4 1-6 2-6 3.5C2 34 10 36 19 36s17-2 17-4.5c0-1.5-2-2.5-6-3.5"/></svg><span>1820 Maple Hollow Rd,<br>Brookfield, OR 97411</span></div>
  <div class="contact-item" style="left:480px;top:200px"><svg width="34" height="34" viewBox="0 0 34 34" fill="none" stroke="#e6c25a" stroke-width="2"><path d="M8 3l5 6-3 4c2 4 6 8 10 10l4-3 6 5-3 5C14 30 4 20 3 6z"/><path d="M20 4a10 10 0 0 1 10 10M20 9a5 5 0 0 1 5 5"/></svg><span>+1 555 018 2247</span></div>
  <div class="contact-item" style="left:754px;top:200px"><svg width="34" height="34" viewBox="0 0 34 34" fill="none" stroke="#e6c25a" stroke-width="2.4"><circle cx="17" cy="17" r="6"/><path d="M23 12v7c0 3 5 3 6-1A13 13 0 1 0 24 28"/></svg><span>support@copperlantern.com</span></div>
</footer>
<div class="brand-badge" style="top:3040px;width:156px;height:156px"><span>COPPER<br>LANTERN</span></div>
<div class="to-top"><svg width="18" height="20" viewBox="0 0 18 20"><path d="M9 19V2M2 9l7-7 7 7" stroke="#1e1409" stroke-width="2.4" fill="none"/></svg></div>
<div class="legal-bar"><span>Copyright © 2022 Copper Lantern. All Rights Reserved</span><span class="pay-list"><span>Tallypay</span><span>Coinrest</span><span>Vexora</span></span></div>

</body>
</html>
```